Local fast-growing company in the service sector

We are looking for a modern business card design, which should also appear on our letterheads

Target Market(s)

Private and industrial sectors

Contact Information for Business Card

Vorname Name
Lindkofer Str. 18
71468 Talbrücken
Tel.: 07163-418259-0
Name@kovaltec-pbz.de

Colors
9d9d9d
919191
aaaaaa

Requirements
Must have
• The logo (file) in silver

```html
<!DOCTYPE html>
<html lang="de">
<head>
<meta charset="utf-8">
<title>Kovaltec – Visitenkarte</title>
<link href="https://fonts.googleapis.com/css2?family=Montserrat:wght@400;500;700&family=Syncopate:wght@700&display=swap" rel="stylesheet">
<style>
  :root {
    --backdrop: #5a5a5a;
    --card-dark: #1f2021;
    --card-mid: #313233;
    --silver: #aaaaaa;
    --silver-light: #d6d6d6;
    --silver-mid: #9d9d9d;
    --text-white: #f4f4f4;
  }
  * { margin: 0; padding: 0; box-sizing: border-box; }
  html, body {
    width: 799px;
    height: 1200px;
    overflow: hidden;
    background: var(--backdrop);
  }
  .sheet {
    width: 799px;
    height: 1200px;
    display: flex;
    flex-direction: column;
    justify-content: space-around;
    align-items: center;
    padding: 60px 0;
  }
  .card {
    position: relative;
    width: 620px;
    height: 354px;
    background: radial-gradient(ellipse at 50% 45%, var(--card-mid) 0%, var(--card-dark) 75%);
    box-shadow: 0 18px 40px rgba(0,0,0,0.45);
    font-family: "Montserrat", sans-serif;
    color: var(--text-white);
  }
  .brand {
    position: absolute;
    display: flex;
    align-items: center;
    gap: 16px;
  }
  .brand-mark {
    width: 34px;
    height: 34px;
    background: var(--silver);
  }
  .brand-text {
    display: flex;
    flex-direction: column;
  }
  .brand-name {
    font-family: "Montserrat", sans-serif;
    font-weight: 700;
    color: var(--silver-light);
    letter-spacing: 1px;
    line-height: 1;
  }
  .brand-web {
    font-family: "Montserrat", sans-serif;
    font-weight: 700;
    color: var(--silver-light);
    line-height: 1.2;
  }
  .card-front .brand {
    left: 50%;
    top: 50%;
    transform: translate(-50%, -50%);
  }
  .card-front .brand-name { font-size: 64px; }
  .card-front .brand-web { font-size: 26px; }
  .card-front .brand-mark { width: 44px; height: 44px; }

  .card-back .brand { left: 52px; top: 50px; }
  .card-back .brand-name { font-size: 44px; }
  .card-back .brand-web { font-size: 18px; }

  .contact {
    position: absolute;
    left: 290px;
    top: 188px;
  }
  .contact-name {
    font-family: "Syncopate", sans-serif;
    font-weight: 700;
    font-size: 18px;
    letter-spacing: 1px;
    margin-bottom: 14px;
    text-transform: uppercase;
  }
  .contact-line {
    display: flex;
    align-items: center;
    gap: 10px;
    font-size: 16px;
    line-height: 25px;
  }
  .contact-line svg { width: 13px; height: 13px; fill: var(--text-white); }
</style>
</head>
<body>
<main class="sheet">
  <section class="card card-front" aria-label="Vorderseite">
    <div class="brand">
      <span class="brand-mark"></span>
      <div class="brand-text">
        <span class="brand-name">KOVALTEC</span>
        <span class="brand-web">kovaltec-pbz.de</span>
      </div>
    </div>
  </section>

  <section class="card card-back" aria-label="Rückseite">
    <div class="brand">
      <span class="brand-mark"></span>
      <div class="brand-text">
        <span class="brand-name">KOVALTEC</span>
        <span class="brand-web">kovaltec-pbz.de</span>
      </div>
    </div>
    <div class="contact">
      <p class="contact-name">Vorname Name</p>
      <p class="contact-line">
        <svg viewBox="0 0 24 24" aria-hidden="true"><path d="M6.6 10.8a15 15 0 0 0 6.6 6.6l2.2-2.2c.3-.3.7-.4 1-.2 1.1.4 2.3.6 3.6.6.6 0 1 .4 1 1V20c0 .6-.4 1-1 1A17 17 0 0 1 3 4c0-.6.4-1 1-1h3.5c.6 0 1 .4 1 1 0 1.3.2 2.5.6 3.6.1.3 0 .7-.2 1z"/></svg>
        07163-418259-0
      </p>
      <p class="contact-line">
        <svg viewBox="0 0 24 24" aria-hidden="true"><path d="M2 5h20v14H2zm2 2v.4l8 5.2 8-5.2V7zm0 2.8V17h16V9.8l-8 5.2z"/></svg>
        Name@kovaltec-pbz.de
      </p>
      <p class="contact-line">Lindkofer Str. 18 71468 Talbrücken</p>
    </div>
  </section>
</main>
</body>
</html>
```